Buff Works Business card design

i need a business card design for my new detailing company called 'Brent's Detail Shop'. i want an all black and white design . simple, direct and to the point. i want the designer to choose a fitting font to match the logothe front should have logo, address, phone and email and the back side should have a slogan and text indicating that we offer services on anything including cars, trucks, motorcycles and RVs. slogan will read "we take pride in your ride"
maybe also very small on the back side the IG icon with Brents_Detail_Shop

phone 208.474.2863
address 3847 E Larkmoor Ave
Spokane WA 98734
email: BrentsDetail@quorvamail.com

Target Market(s)

all ages , auto enthusiasts

Industry/Entity Type

Automotive

Contact Information for Business Card

the front should have logo, address, phone and email and the back side should have a slogan and text indicating that we offer services on anything including cars, trucks, motorcycles and RVs. slogan will read "we take pride in your ride"

phone 208.474.2863
address 3847 E Larkmoor Ave
Spokane WA 98734

Colors
000000
ffffff

Requirements
Must have
• bold font and very simple design with good spacing
Nice to have
• anything creative from the designer indicating we service any types of vehicles
Should not have
• any colors ,

```html
<!DOCTYPE html>
<html lang="en">
<head>
<meta charset="utf-8">
<title>Brent's Detail Shop – Business Card</title>
<link rel="stylesheet" href="https://fonts.googleapis.com/css2?family=Noto+Serif:wght@400;700&display=swap">
<style>
  :root {
    --ink: #000000;
    --paper: #ffffff;
    --stage: #2a2c2f;
    --muted: #bdbdbd;
    --ghost: rgba(255,255,255,0.07);
  }
  * { box-sizing: border-box; margin: 0; padding: 0; }
  html, body { width: 1200px; height: 900px; overflow: hidden; }
  body {
    background: var(--stage);
    font-family: "Noto Serif", Georgia, serif;
    display: flex;
    align-items: center;
    justify-content: center;
    gap: 40px;
  }
  .card {
    position: relative;
    width: 520px;
    height: 297px;
    border-radius: 22px;
    overflow: hidden;
    background: var(--ink);
    color: var(--paper);
  }
  .card-shapes { position: absolute; inset: 0; width: 100%; height: 100%; }

  /* Front */
  .brand-mark {
    position: absolute;
    left: 22px; top: 0; width: 190px; height: 100%;
    display: flex; align-items: center; justify-content: center;
    text-align: center;
    color: var(--ink);
    font-weight: 700;
    font-size: 26px;
    line-height: 1.15;
  }
  .contact {
    position: absolute;
    right: 18px; top: 0; width: 250px; height: 100%;
    display: flex; flex-direction: column; align-items: center; justify-content: center;
    text-align: center;
  }
  .contact-name { font-weight: 700; font-size: 23px; letter-spacing: 0.3px; }
  .contact-role { font-size: 13px; margin-top: 1px; }
  .contact-rule { width: 70px; height: 2px; background: var(--paper); margin: 14px 0; }
  .contact-line { font-size: 15px; line-height: 1.35; }

  /* Back */
  .ghost-name {
    position: absolute; inset: 0;
    display: flex; align-items: center; justify-content: center;
    font-weight: 700; font-size: 40px; color: var(--ghost);
  }
  .slogan {
    position: absolute; top: 24px; right: 30px;
    font-size: 13px; letter-spacing: 1.5px; font-variant: small-caps;
  }
  .services {
    position: absolute; top: 86px; left: 30px; right: 30px;
    display: flex; justify-content: space-between;
    list-style: none;
    font-weight: 700; font-size: 21px;
  }
  .services li { display: flex; align-items: center; gap: 7px; }
  .services li::before {
    content: ""; width: 13px; height: 13px; border-radius: 50%; background: var(--paper);
  }
  .social {
    position: absolute; left: 40px; bottom: 28px;
    display: flex; align-items: center; gap: 9px;
    color: var(--ink); font-weight: 700; font-size: 14px;
  }
  .social-square { width: 16px; height: 16px; background: var(--ink); border-radius: 3px; }
</style>
</head>
<body>

  <section class="card card-front" aria-label="Card front">
    <svg class="card-shapes" viewBox="0 0 520 297" aria-hidden="true">
      <polygon points="0,0 250,0 190,297 0,297" fill="#ffffff"/>
      <polygon points="262,0 274,0 214,297 202,297" fill="#ffffff"/>
    </svg>
    <div class="brand-mark">Brent's<br>Detail Shop</div>
    <div class="contact">
      <p class="contact-name">Dale Harmon</p>
      <p class="contact-role">Owner</p>
      <span class="contact-rule"></span>
      <p class="contact-line">208.474.2863</p>
      <p class="contact-line">BrentsDetail@quorvamail.com</p>
      <span class="contact-rule"></span>
      <p class="contact-line">3847 E Larkmoor Ave</p>
      <p class="contact-line">Spokane WA 98734</p>
    </div>
  </section>

  <section class="card card-back" aria-label="Card back">
    <div class="ghost-name" aria-hidden="true">Brent's Detail Shop</div>
    <svg class="card-shapes" viewBox="0 0 520 297" aria-hidden="true">
      <polygon points="0,205 330,205 300,297 0,297" fill="#ffffff"/>
      <line x1="345" y1="205" x2="520" y2="205" stroke="#ffffff" stroke-width="3"/>
    </svg>
    <p class="slogan">We Take Pride In Your Ride</p>
    <ul class="services">
      <li>Auto</li>
      <li>Motorcycle</li>
      <li>Boat</li>
      <li>RV</li>
    </ul>
    <div class="social">
      <span class="social-square"></span>
      <span>Brents_Detail_Shop</span>
    </div>
  </section>

</body>
</html>
```